Trifold Leaflet - Osteopathy

Trifold Leaflet (A4 size paper) to provide information and promote an established English seafront osteopathy clinic.
I would like a simple modern design to reflect the seafront location and the caring nature of osteopathy treatment. The design needs to be not be generic or too corporate.
At the top of the front page in a large font should be the word "Osteopathy" as it will be displayed in a rack of leaflets (photo attached) and needs to be eye-catching.
I have attached a logo file and some examples of the kinds of designs that I like- but i'm very open to your expert ideas!
Also attached is a photo of the location- a bit of an ugly building but right on the beach, it would be great if this location could be emphasized!
The Word files: Leaflets word-inside.doc & Leaflets word-outside.doc uploaded show the content that I'd like- this is definitely not set in stone and I appreciate that less content is probably needed. Feel free to include/leave out whatever you feel is right.
More info on the practice can be found on my website:
www.harrowdenbackcare.com
The shutterstock images are ones that I have previously bought the rights to use, but only use them if you think they suit you design- I have included them i case they are of use to you.
Target Market(s)
Any adult.
Industry/Entity Type
Building
Look and feel
Each slider illustrates characteristics of the customer's brand and the style your logo design should communicate.

```html
<!DOCTYPE html>
<html lang="en">
<head>
<meta charset="utf-8">
<title>Osteopathy Leaflet – Inside Spread</title>
<link href="https://fonts.googleapis.com/css2?family=PT+Sans:wght@400;700&family=PT+Sans+Narrow:wght@700&display=swap" rel="stylesheet">
<style>
  :root {
    --red: #e81f25;
    --ink: #2f2f2f;
    --white: #ffffff;
    --strip: #9a9a9a;
    --paper: #ffffff;
    --muted: #7d7d7d;
  }
  * { margin: 0; padding: 0; box-sizing: border-box; }
  html, body { width: 1200px; height: 930px; overflow: hidden; background: var(--paper); }
  body { font-family: "PT Sans", sans-serif; color: var(--ink); }
  .spread { position: relative; width: 1200px; height: 930px; overflow: hidden; background: var(--paper); }
  .side-strip { position: absolute; left: 0; top: 0; width: 28px; height: 930px; background: var(--strip); }

  .photo { position: absolute; background: var(--white); padding: 9px; box-shadow: 0 2px 8px rgba(0,0,0,.35); }
  .photo .fill { width: 100%; height: 100%; }
  .backing { position: absolute; }

  .col { position: absolute; font-size: 15px; line-height: 22.6px; text-align: justify; }
  .col p { margin-bottom: 8px; }
  .heading { font-family: "PT Sans Narrow", sans-serif; font-weight: 700; color: var(--red); text-align: center; font-size: 25px; line-height: 31px; }
  .sub { font-weight: 700; text-align: left; }
  .conditions { font-weight: 700; text-align: left; }

  .col-left { left: 44px; top: 322px; width: 341px; }
  .col-middle { left: 417px; top: 36px; width: 360px; }
  .col-right { left: 819px; top: 303px; width: 342px; height: 520px; overflow: hidden; }

  .partner { position: absolute; left: 447px; top: 672px; width: 148px; text-align: center; }
  .partner-mark { width: 52px; height: 52px; border-radius: 50%; border: 3px solid var(--red); margin: 0 auto 10px; }
  .partner-name { color: #1f3a6d; font-size: 16px; line-height: 20px; }
  .partner-rule { position: absolute; left: 449px; top: 789px; width: 146px; height: 1px; background: #1f3a6d; }
  .badge { position: absolute; left: 641px; top: 664px; width: 102px; height: 130px; border: 3px solid #111; background: #111; }

  .band { position: absolute; left: 28px; top: 823px; width: 1172px; height: 107px; background: var(--red); }
  .contact { position: absolute; left: 400px; top: 827px; width: 400px; text-align: center; color: var(--white); }
  .contact .venue { font-size: 18px; line-height: 21px; }
  .contact .phone { font-family: "PT Sans", sans-serif; font-weight: 700; font-size: 47px; line-height: 54px; letter-spacing: 0.5px; }
  .band-note { position: absolute; left: 819px; top: 832px; width: 342px; color: var(--white); font-size: 15px; line-height: 22px; text-align: justify; }
</style>
</head>
<body>
<main class="spread">
  <div class="side-strip"></div>

  <!-- left column images -->
  <div class="photo" style="left:36px;top:34px;width:330px;height:276px;transform:rotate(3deg);"><div class="fill" style="background:#222"></div></div>
  <div class="photo" style="left:40px;top:30px;width:332px;height:270px;transform:rotate(1.5deg);"><div class="fill" style="background:#333"></div></div>
  <div class="photo" style="left:44px;top:20px;width:340px;height:256px;">
    <div class="fill" role="img" aria-label="Man's bare back with lower back pain highlighted in red" style="background:radial-gradient(circle at 50% 70%, #d85a3a 0, #9a7a70 22%, #6a6a6a 55%, #cfcfcf 100%);"></div>
  </div>

  <section class="col col-left">
    <p>Much of the pain and disablity we suffer stems from abnormalities in our body's structure and function.</p>
    <p>Osteopathy treats problems related to the musculoskeletal system, muscles, ligaments, nerves and joints, and helps the body's natural healing ability to correct itself and releive the pain caused by dysfunction.</p>
    <p>When the body is balanced and efficient, just like a tuned engine, it will function with minimum wear and tear, requiring less energy to operate correctly.</p>
    <p style="margin-bottom:2px;text-align:left">Natural, Drug Free, Pain Relief</p>
    <p class="conditions">Treating: Arthritis &amp; Joint Pain, Back &amp; Neck Pain Frozen Shoulder, Sports Injury, Sciatica</p>
  </section>

  <div class="photo" style="left:2px;top:710px;width:200px;height:200px;transform:rotate(-8deg);">
    <div class="fill" role="img" aria-label="Anatomy illustration of hip and leg muscles" style="background:linear-gradient(135deg,#c9806a,#e9c6b4 60%,#f2e1d6);"></div>
  </div>
  <div class="photo" style="left:150px;top:690px;width:240px;height:210px;transform:rotate(5deg);">
    <div class="fill" role="img" aria-label="Medical illustration of the spine with neck highlighted" style="background:linear-gradient(160deg,#eef3f7,#bcd3e6 55%,#e66a5a);"></div>
  </div>
  <div class="photo" style="left:112px;top:812px;width:220px;height:140px;transform:rotate(-3deg);">
    <div class="fill" role="img" aria-label="X-ray style image of a glowing spine" style="background:radial-gradient(circle at 55% 60%, #e23a3a 0, #1d3a6a 35%, #061226 100%);"></div>
  </div>

  <!-- middle column -->
  <section class="col col-middle">
    <h2 class="heading" style="margin-bottom:12px;">Osteopathy&nbsp; is Regulated and safe</h2>
    <p>Osteopathy is one of only two complementary and alternative medicines (CAMs) that are regulated under UK law. This regulation works in much the same way as regulation for medical doctors.</p>
    <p>The OPC regulates the Osteopathic profession in the UK, maintaining a Statutory Register of those entitled to practise. Only practitioners meeting the high standards of safety and competency are eligible to join this register. All</p>
    <p>Osteopaths are required to undertake a certain amount of CPD (Continuing Professional Development) each year to keep up to date with new research and practise within the profession.</p>
    <h2 class="heading" style="margin:22px 0 14px;">As Recommended by<br>The College of Family Doctors</h2>
    <p>Osteopathy is used to treat many problems related to the musculoskeletal system. Osteopathic manipulation has been recommended by The National Centre for Care Standards (NCCS) and The College of Family Doctors (CFD) for the treatment of low back pain.</p>
  </section>

  <div class="partner">
    <div class="partner-mark"></div>
    <div class="partner-name">Coastal Osteopathic Society</div>
  </div>
  <div class="partner-rule"></div>
  <div class="badge" role="img" aria-label="Registration certification badge"></div>

  <!-- right column image -->
  <div class="backing" style="left:830px;top:22px;width:330px;height:262px;background:#6e6e6e;transform:rotate(5deg);"></div>
  <div class="backing" style="left:818px;top:30px;width:340px;height:250px;background:var(--red);transform:rotate(-2deg);"></div>
  <div class="photo" style="left:810px;top:24px;width:356px;height:262px;">
    <div class="fill" role="img" aria-label="Osteopath treating a patient lying on a treatment couch" style="background:linear-gradient(120deg,#9c9c9c,#d9c7b8 45%,#f2efec 75%,#e8e2dc);"></div>
  </div>

  <section class="col col-right">
    <h2 class="heading" style="margin-bottom:8px;">Your first visit</h2>
    <p class="sub" style="margin-bottom:2px;">Medical History</p>
    <p style="margin-bottom:2px;">On your first visit, we will ask you lots of questions to build up a detailed medical history. Your past medical history can often be relevant to current problems you are experiencing and may be discussed. We may ask about past illnesses, operations, injuries, accidents and medications.</p>
    <p class="sub" style="margin-bottom:2px;">Assessment</p>
    <p style="margin-bottom:2px;">Based on your&nbsp; medical history, we will perform some tests to help form a diagnosis of your current condition. Typical tests include range and quality of joint movments, tenderness to palpation, muscle tone and strength, reflexes and blood pressure.</p>
    <p class="sub" style="margin-bottom:2px;">Treatment</p>
    <p>Supported by an in depth knowledge of functional anatomy and physiology the detailed examination enables the Osteopath to diagnose safely and choose the right treatment to address the causes of the patient's symptoms. Treatment involves gentle, manual techniques – easing pain,</p>
  </section>

  <!-- footer band -->
  <footer class="band"></footer>
  <div class="contact">
    <div class="venue">Shoreline Wellness Centre</div>
    <div class="venue">Marine Parade, Harrowden, HD4 2QX</div>
    <div class="phone">01632 960418</div>
  </div>
  <p class="band-note">Osteopathy is a ‘package’ of care that includes skilled mobilising and manipulative techniques, reinforced by guidance on diet and exercise.</p>
</main>
</body>
</html>
```